stationary deign for trucking company

im a trucking company looking for a professional set of stationary designs i deliver goods from point a to b
Updates

When submitting stationary designs I need envelope design, letterhead, cards, I’d badge etc

Industry/Entity Type

Trucking Company

Requirements
Must have
• must have letter head, business card, envelope, fax sheet, id badge, folder, thank you card, notebook, invoice sheet.
Nice to have
• nice to have them all custom made (letterhead,envelope, business card, I’d badge etc
Should not have
• must not have prepaid sign want i unique design for items

```html
<!DOCTYPE html>
<html lang="en">
<head>
<meta charset="utf-8">
<title>Harlow Freight Logistics – Stationery Set</title>
<link rel="stylesheet" href="https://fonts.googleapis.com/css2?family=Montserrat:wght@400;500;600&family=Open+Sans:wght@400&display=swap">
<style>
:root{
  --bg:#e6e7e6;
  --paper:#ffffff;
  --ink:#111418;
  --black:#0a0a0b;
  --blue:#1f5fb5;
  --label:#1f3f6e;
  --muted:#5b6068;
  --faint:#dfe6ef;
  --faint-grey:#e4e4e4;
}
*{box-sizing:border-box;margin:0;padding:0}
html,body{width:1200px;height:2329px;overflow:hidden}
body{background:var(--bg);position:relative;font-family:"Montserrat",sans-serif;color:var(--ink)}
.item{position:absolute;background:var(--paper);box-shadow:0 3px 10px rgba(0,0,0,.18);overflow:hidden}
.label{position:absolute;font-family:"Open Sans",sans-serif;font-size:20px;color:var(--label)}

/* brand lockup */
.brand{display:flex;align-items:center;gap:.45em;color:var(--ink);font-weight:500}
.brand-square{width:1.05em;height:1.05em;border:.09em solid currentColor;flex:none}
.brand-text{display:flex;flex-direction:column;line-height:1}
.brand-name{font-size:1em;letter-spacing:.08em}
.brand-tag{font-size:.3em;letter-spacing:.2em;margin-top:.35em}
.brand.on-dark{color:#fff}
.brand.blue{color:var(--blue)}

/* faint large wordmark */
.ghost{position:absolute;font-weight:500;letter-spacing:.08em;color:var(--faint);line-height:1}

/* business cards */
.card-front{left:113px;top:112px;width:207px;height:116px}
.card-front .brand{position:absolute;left:72px;top:14px;font-size:15px}
.card-front .bar{position:absolute;left:0;top:56px;width:4px;height:14px;background:var(--blue)}
.card-front .name{position:absolute;left:12px;top:56px;font-size:7px;font-weight:600;color:var(--blue)}
.card-front .role{position:absolute;left:12px;top:65px;font-size:4.5px;color:var(--muted)}
.card-front .rule{position:absolute;left:12px;right:12px;top:74px;height:1px;background:#ccc}
.card-front .lines{position:absolute;left:12px;top:80px;font-size:4.5px;line-height:7px;color:var(--muted)}
.card-front .addr{position:absolute;left:120px;top:80px;font-size:4.5px;line-height:7px;color:var(--muted)}
.card-front .addr b{color:var(--blue);font-weight:600}
.card-back{left:356px;top:112px;width:206px;height:116px;background:var(--black);display:flex;align-items:center;justify-content:center}
.card-back .brand{font-size:18px}

/* letterheads */
.letter{top:287px;height:599px}
.letter-a{left:123px;width:423px}
.letter-b{left:630px;width:465px}
.letter .brand{position:absolute;left:50%;top:46px;transform:translateX(-50%);font-size:26px}
.letter .ghost{left:50%;top:50%;transform:translate(-50%,-50%);font-size:92px}
.letter-foot{position:absolute;left:0;right:0;bottom:22px;text-align:center;font-size:7px;color:var(--muted);line-height:12px}
.letter-foot b{color:var(--blue);font-weight:600}
.letter-foot svg{width:7px;height:7px;vertical-align:-1px;fill:var(--blue)}
.letter-b .recipient{position:absolute;left:30px;top:168px;font-size:8.5px;line-height:13px;color:var(--muted)}
.letter-b .recipient strong{color:var(--blue);font-weight:500;font-size:10.5px}
.letter-b .date{position:absolute;right:30px;top:168px;font-size:9px;color:var(--muted)}
.letter-b .body{position:absolute;left:30px;right:30px;top:250px;font-size:8.4px;line-height:14px;color:#555}
.letter-b .body p+p{margin-top:14px}
.letter-b .closing{position:absolute;left:30px;top:426px;font-size:7px;color:#555}
.letter-b .signature{position:absolute;left:30px;top:440px;width:50px;height:14px;background:#eceef1}
.letter-b .signer{position:absolute;left:30px;top:470px;font-size:7px;color:#555}

/* envelopes */
.envelope{width:451px;height:200px}
.env-a{left:113px;top:1032px}
.env-b{left:610px;top:1032px}
.env-c{left:113px;top:1268px;height:199px}
.env-a .brand{position:absolute;left:28px;top:28px;font-size:21px}
.env-a .addr{position:absolute;left:28px;top:74px;font-size:8px;color:var(--muted)}
.env-a .addr svg{width:8px;height:9px;fill:var(--blue);vertical-align:-1px}
.env-a .ghost{right:14px;bottom:22px;font-size:26px;color:var(--faint-grey)}
.flap{position:absolute;left:0;top:0;width:100%;height:86px}
.flap-mark{position:absolute;left:50%;top:22px;transform:translateX(-50%);font-size:17px}

/* id badge */
.lanyard{position:absolute;left:801px;top:1234px;width:14px;height:38px;background:var(--blue)}
.badge{left:731px;top:1265px;width:149px;height:225px;border-radius:10px;border:5px solid #f1f1f1}
.badge .clip{position:absolute;left:50%;top:8px;transform:translateX(-50%);width:30px;height:6px;border-radius:3px;background:#d4d4d4}
.badge .brand{position:absolute;left:28px;top:26px;font-size:12px}
.badge .photo{position:absolute;left:46px;top:60px;width:48px;height:52px;background:linear-gradient(#c9ced6,#8d96a3)}
.badge .name{position:absolute;left:0;right:0;top:120px;text-align:center;font-size:7px;font-weight:600;color:var(--blue)}
.badge .role{position:absolute;left:0;right:0;top:129px;text-align:center;font-size:4.5px;color:var(--muted)}
.badge .fields{position:absolute;left:18px;top:142px;font-size:4.5px;line-height:8px;color:var(--muted)}
.badge .fields b{display:inline-block;width:22px;color:var(--blue);font-weight:600}

/* folder */
.folder{position:absolute;left:113px;top:1511px;width:927px;height:745px}
.f-side{position:absolute;top:0;width:36px;height:543px;background:var(--black)}
.f-side.left{left:0;border-radius:6px 0 0 6px}
.f-side.right{right:0;border-radius:0 6px 6px 0}
.notch{position:absolute;top:178px;width:20px;height:30px;background:var(--bg);border-radius:50%}
.f-side.left .notch{left:-10px}
.f-side.right .notch{right:-10px}
.f-back{position:absolute;left:36px;top:0;width:429px;height:543px;background:var(--black);overflow:hidden}
.f-back .ghost{left:50%;top:210px;transform:translateX(-50%);font-size:78px;color:#111a28}
.f-contact{position:absolute;left:33px;top:417px;color:#fff;font-size:10px;line-height:15px}
.f-contact h2{font-weight:400;font-size:15px;color:var(--blue);padding-bottom:4px;border-bottom:1.5px solid var(--blue);width:124px;margin-bottom:10px}
.f-contact svg{width:9px;height:9px;fill:var(--blue);vertical-align:-1px;margin-right:5px}
.f-contact .web span{color:var(--blue)}
.f-front{position:absolute;left:465px;top:0;width:428px;height:543px;background:var(--paper)}
.f-front .brand{position:absolute;left:50%;top:248px;transform:translateX(-50%);font-size:32px}
.f-tab{position:absolute;right:0;top:380px;width:25px;height:163px;background:var(--blue);border-radius:10px 0 0 0}
.f-tab span{position:absolute;left:50%;top:50%;transform:translate(-50%,-50%) rotate(-90deg);white-space:nowrap;color:#fff;font-size:8px}
.pocket{position:absolute;top:543px;height:202px;background:var(--black);border-radius:0 0 18px 18px}
.pocket.left{left:36px;width:418px}
.pocket.right{left:496px;width:397px;border-radius:0 0 18px 40px}
.mini-card{position:absolute;left:152px;top:61px;width:140px;height:82px;background:var(--paper)}
.mini-card .brand{position:absolute;left:46px;top:10px;font-size:11px}
.mini-card .name{position:absolute;left:6px;top:40px;font-size:5px;font-weight:600;color:var(--blue)}
.mini-card .lines{position:absolute;left:6px;top:48px;font-size:3.5px;line-height:5.5px;color:var(--muted)}
</style>
</head>
<body>

<!-- business cards -->
<div class="item card-front">
  <div class="brand"><span class="brand-square"></span><span class="brand-text"><span class="brand-name">HARLOW</span><span class="brand-tag">FREIGHT · LOGISTICS</span></span></div>
  <span class="bar"></span>
  <div class="name">DAN WHITCOMBE</div>
  <div class="role">Senior Consultant</div>
  <span class="rule"></span>
  <div class="lines">(410) 555-0182<br>info@harlowfreight.com<br>www.harlowfreight.com</div>
  <div class="addr"><b>HARLOW</b><br>420 Harbor Rd. Ste 12B<br>Easton, MD 21601</div>
</div>
<div class="item card-back">
  <div class="brand blue"><span class="brand-square"></span><span class="brand-name">HARLOW</span></div>
</div>

<!-- letterheads -->
<div class="item letter letter-a">
  <div class="brand"><span class="brand-square"></span><span class="brand-text"><span class="brand-name">HARLOW</span><span class="brand-tag">FREIGHT · LOGISTICS</span></span></div>
  <div class="ghost">HARLOW</div>
  <div class="letter-foot">
    <b>HARLOW</b> • 420 Harbor Rd. Ste 12B Easton, MD 21601<br>
    <svg viewBox="0 0 10 10"><path d="M2 0h2l1 3-1.5 1a6 6 0 0 0 2.5 2.5L7 5l3 1v2c0 1-1 2-2 2A8 8 0 0 1 0 2c0-1 1-2 2-2z"/></svg> (410) 555-0182 |
    <svg viewBox="0 0 10 10"><path d="M0 2h10v6H0zM0 2l5 3 5-3"/></svg> info@harlowfreight.com |
    <svg viewBox="0 0 10 10"><circle cx="5" cy="5" r="5"/></svg> www.harlowfreight.com
  </div>
</div>
<div class="label" style="left:256px;top:922px">Letterhead</div>

<div class="item letter letter-b">
  <div class="brand"><span class="brand-square"></span><span class="brand-text"><span class="brand-name">HARLOW</span><span class="brand-tag">FREIGHT · LOGISTICS</span></span></div>
  <div class="ghost">HARLOW</div>
  <div class="recipient"><strong>Dan Whitcombe</strong><br>Manager<br>88 Mill Lane<br>Ashford, NC</div>
  <div class="date">Date: 31/01/2019</div>
  <div class="body">
    <p>Lorem ipsum dolor sit amet, consectetuer adipiscing elit, sed diam nonummy nibh euismod tincidunt ut laoreet dolore magna aliquam erat volutpat. Ut wisi enim ad minim veniam, quis nostrud exerci tation ullamcorper suscipit lobortis nisl ut aliquip ex ea commodo consequat. Lorem ipsum dolor sit amet, cons ectetuer adipiscing elit, sed diam nonummy nibh euismod tincidunt ut laoreet dolore magna aliquam erat volutpat. Ut wisi enim ad minim veniam, quis nostrud exerci tation ullamcorper suscipit lobortis nisl ut aliquip ex ea commodo consequat. Lorem ipsum dolor sit amet, consectetuer adipiscing elit, sed diam nonummy nibh euismod tincidunt ut laoreet dolore magna aliquam erat volutpat. Ut wisi enim ad minim veniam,</p>
    <p>consequat. Duis autem vel eum iriure dolor in hendrerit in vulputate velit esse molestie consequat, vel illum dolore eu feugiat nulla facilisis at vero eros et accumsan .</p>
  </div>
  <div class="closing">sincerely</div>
  <div class="signature" role="img" aria-label="Handwritten signature"></div>
  <div class="signer">Owen Pratt</div>
  <div class="letter-foot">
    <b>HARLOW</b> • 420 Harbor Rd. Ste 12B Easton, MD 21601<br>
    <svg viewBox="0 0 10 10"><path d="M2 0h2l1 3-1.5 1a6 6 0 0 0 2.5 2.5L7 5l3 1v2c0 1-1 2-2 2A8 8 0 0 1 0 2c0-1 1-2 2-2z"/></svg> (410) 555-0182 |
    <svg viewBox="0 0 10 10"><path d="M0 2h10v6H0zM0 2l5 3 5-3"/></svg> info@harlowfreight.com |
    <svg viewBox="0 0 10 10"><circle cx="5" cy="5" r="5"/></svg> www.harlowfreight.com
  </div>
</div>
<div class="label" style="left:759px;top:922px">Word Document Letterhead</div>

<div class="label" style="left:259px;top:977px">Envelope</div>
<div class="label" style="left:767px;top:977px">Envelope</div>

<!-- envelopes -->
<div class="item envelope env-a">
  <div class="brand"><span class="brand-square"></span><span class="brand-text"><span class="brand-name">HARLOW</span><span class="brand-tag">FREIGHT · LOGISTICS</span></span></div>
  <div class="addr"><svg viewBox="0 0 8 10"><path d="M4 0a4 4 0 0 1 4 4c0 3-4 6-4 6S0 7 0 4a4 4 0 0 1 4-4z"/></svg> 420 Harbor Rd. Ste 12B Easton, MD 21601</div>
  <div class="ghost">HARLOW</div>
</div>

<div class="item envelope env-b">
  <svg class="flap" viewBox="0 0 451 86" preserveAspectRatio="none"><path d="M0 0h451v30l-10 56H10L0 30z" fill="#0a0a0b"/></svg>
  <div class="flap-mark brand blue"><span class="brand-square"></span><span class="brand-name">HARLOW</span></div>
</div>

<div class="item envelope env-c">
  <svg class="flap" viewBox="0 0 451 86" preserveAspectRatio="none"><path d="M0 0h451v30l-10 56H10L0 30z" fill="#0a0a0b"/></svg>
  <div class="flap-mark brand on-dark"><span class="brand-square"></span><span class="brand-name">HARLOW</span></div>
</div>
<div class="label" style="left:576px;top:1355px">Envelope</div>

<!-- id badge -->
<span class="lanyard"></span>
<div class="item badge">
  <span class="clip"></span>
  <div class="brand"><span class="brand-square"></span><span class="brand-text"><span class="brand-name">HARLOW</span><span class="brand-tag">FREIGHT · LOGISTICS</span></span></div>
  <div class="photo" role="img" aria-label="Staff portrait photo"></div>
  <div class="name">DAN WHITCOMBE</div>
  <div class="role">Senior Consultant</div>
  <div class="fields"><b>ID No</b>: 0294<br><b>Email</b>: info@harlowfreight.com<br><b>Phone</b>: (410) 555-0182<br><b>Blood</b>: O+</div>
</div>
<div class="label" style="left:942px;top:1355px">Id Card</div>

<!-- folder -->
<div class="folder">
  <div class="f-side left"><span class="notch"></span></div>
  <div class="f-back">
    <div class="ghost">HARLOW</div>
    <div class="f-contact">
      <h2>Contact Info</h2>
      PO Box 4471, Dunmore<br>VIC 3190<br>
      <div style="margin-top:6px"><svg viewBox="0 0 10 10"><path d="M2 0h2l1 3-1.5 1a6 6 0 0 0 2.5 2.5L7 5l3 1v2c0 1-1 2-2 2A8 8 0 0 1 0 2c0-1 1-2 2-2z"/></svg>+0400 555 318</div>
      <div><svg viewBox="0 0 10 10"><path d="M0 2h10v6H0z"/></svg>hello@harlowfreight.com</div>
      <div class="web"><svg viewBox="0 0 10 10"><circle cx="5" cy="5" r="5"/></svg>www.<span>harlowfreight</span>.com</div>
    </div>
  </div>
  <div class="f-front">
    <div class="brand"><span class="brand-square"></span><span class="brand-text"><span class="brand-name">HARLOW</span><span class="brand-tag">FREIGHT · LOGISTICS</span></span></div>
    <div class="f-tab"><span>www.harlowfreight.com</span></div>
  </div>
  <div class="f-side right"><span class="notch"></span></div>
  <div class="pocket left"></div>
  <div class="pocket right">
    <div class="mini-card">
      <div class="brand"><span class="brand-square"></span><span class="brand-text"><span class="brand-name">HARLOW</span><span class="brand-tag">FREIGHT · LOGISTICS</span></span></div>
      <div class="name">DAN WHITCOMBE</div>
      <div class="lines">Senior Consultant<br>(410) 555-0182<br>info@harlowfreight.com<br>www.harlowfreight.com</div>
    </div>
  </div>
</div>
<div class="label" style="left:1039px;top:2127px">Folder</div>

</body>
</html>
```